I need a mobile phone and tablet review site.

Hi everyone, I am looking for a professionally designed website which will review newly produced mobile phone and tablets. In the website users should be able to comment about newly produced phones. The website is to resemble gadget parlor. Which also review Mobile phones. There would be a category for tablets and a different category for mobile phone in the website. Under the Mobile category there should be a column for popular brands like Torvo, Velmira and others. Same thing goes for the tablet category. My site should be eye catching.

```html
<!DOCTYPE html>
<html lang="en">
<head>
<meta charset="utf-8">
<title>Handset Den – About</title>
<link href="https://fonts.googleapis.com/css2?family=Lato:wght@400;700&display=swap" rel="stylesheet">
<style>
:root{
  --blue:#0f40c4;
  --blue-active:#2a5fdc;
  --blue-link:#1d4fc9;
  --page:#f3f3f3;
  --ink:#1c1c1c;
  --muted:#777;
  --rule:#d6d6d6;
  --footer:#1c1c1c;
  --footer-text:#a9a9a9;
}
*{margin:0;padding:0;box-sizing:border-box}
html,body{width:839px;height:1200px;overflow:hidden}
body{position:relative;background:var(--page);font-family:'Lato',sans-serif;color:var(--ink)}
.site-header{position:absolute;left:0;top:0;width:839px;height:74px;background:var(--blue)}
.brand{position:absolute;left:56px;top:24px;color:#fff;font-size:24px;font-weight:700;line-height:26px}
.main-nav a{position:absolute;top:0;height:74px;line-height:76px;color:#fff;font-size:13.5px;font-weight:700;text-decoration:none}
.main-nav .active{background:var(--blue-active);padding:0 9px}
.search-icon{position:absolute;left:770px;top:30px}
.breadcrumb-bar{position:absolute;left:56px;top:86px;width:728px;height:51px;background:var(--blue);color:#fff;padding:11px 11px}
.breadcrumb-bar h1{font-size:12px;font-weight:700;line-height:14px}
.crumbs{font-size:8.5px;font-weight:700;margin-top:3px}
.crumbs span{color:#8fb0ff;font-weight:400}
.section-title{position:absolute;font-size:18px;font-weight:700;line-height:20px;padding-bottom:6px;border-bottom:2px solid var(--ink)}
.photo{position:absolute}
.blue-head{position:absolute;color:var(--blue-link);font-size:12px;font-weight:700;line-height:17px}
.copy{position:absolute;color:var(--muted);font-size:7.3px;line-height:12px}
.read-more{position:absolute;font-size:8px;color:var(--ink);text-decoration:underline}
.news-rule{position:absolute;height:1px;background:var(--rule)}
.blog-item{position:absolute;left:430px;width:167px;border-bottom:1px solid var(--rule)}
.blog-item .thumb{position:absolute;left:0;top:0;width:43px;height:46px}
.blog-item h3{margin-left:48px;font-size:9.6px;font-weight:400;line-height:17px;text-transform:uppercase}
.blog-item p{margin-left:48px;margin-top:2px;font-size:6.8px;line-height:12px;color:var(--muted)}
.popular{position:absolute;left:616px;top:167px;width:168px}
.popular-head{height:50px;background:var(--blue);color:#fff;font-size:12px;font-weight:700;line-height:17px;padding:8px 11px}
.popular-list{background:#fff;height:652px;padding:4px 10px}
.product{height:128px;margin-bottom:2px;border-radius:4px}
.site-footer{position:absolute;left:0;top:938px;width:839px;height:262px;background:var(--footer)}
.foot-head{position:absolute;top:28px;color:#fff;font-size:12px;font-weight:700}
.foot-list{position:absolute;top:53px;list-style:none}
.foot-list li{font-size:8.5px;line-height:20px;color:var(--footer-text);text-transform:uppercase}
.foot-list .current{color:var(--blue-active)}
.social{position:absolute;left:429px;width:120px;height:26px}
.social .dot{position:absolute;left:0;top:0;width:26px;height:26px;border-radius:50%;background:var(--blue)}
.social span{position:absolute;left:37px;top:8px;font-size:8.5px;color:var(--footer-text)}
.foot-rule{position:absolute;left:56px;top:211px;width:728px;height:1px;background:#333}
.copyright{position:absolute;left:56px;top:222px;font-size:7px;color:#8a8a8a}
.to-top{position:absolute;left:795px;top:205px}
</style>
</head>
<body>

<header class="site-header">
  <div class="brand">Handset Den</div>
  <nav class="main-nav">
    <a style="left:422px">HOME</a>
    <a class="active" style="left:473px">ABOUT</a>
    <a style="left:549px">NEWS</a>
    <a style="left:607px">REVIEWS</a>
    <a style="left:686px">CONTACTS</a>
  </nav>
  <svg class="search-icon" width="13" height="13" viewBox="0 0 13 13"><circle cx="5.5" cy="5.5" r="4" fill="none" stroke="#fff" stroke-width="2"/><line x1="8.5" y1="8.5" x2="12" y2="12" stroke="#fff" stroke-width="2.2" stroke-linecap="round"/></svg>
</header>

<div class="breadcrumb-bar">
  <h1>ABOUT</h1>
  <div class="crumbs">HOME &nbsp;| &nbsp;<span>ABOUT</span></div>
</div>

<h2 class="section-title" style="left:56px;top:165px;width:354px">ABOUT US</h2>
<div class="photo" role="img" aria-label="Hands using a tablet" style="left:56px;top:207px;width:354px;height:179px;background:linear-gradient(135deg,#bfd0e2 0%,#e9dccd 45%,#d9c2ad 65%,#4f6f9c 100%)"></div>
<div class="blue-head" style="left:56px;top:401px;width:354px">LACUS EU FEUGIAT MALESUADA. NUNC VITAE EROS LOREM. SUSPENDISSE ELEMENTUM MAXIMUS</div>
<p class="copy" style="left:56px;top:437px;width:354px">Aliquam ullamcorper lacus eu feugiat malesuada. Nunc vitae eros lorem. Suspendisse elementum maximus turpis vel suscipit. Nullam dapibus, ligula vitae feugiat hendrerit, nisl neque gravida nunc, sed viverra dui augue eget libero. Nulla ut quam lacus. Proin lacinia erat ac ullamcorper luctus. Nam condimentum eu est quis mattis. Ut non tortor sodales, viverra felis eu, egestas felis. Nullam dapibus posuere nunc. Cras at pulvinar purus, eleifend elementum est. Vivamus feugiat ullamcorper velit vehic</p>

<h2 class="section-title" style="left:56px;top:522px;width:354px">GADGET NEWS</h2>
<div class="photo" role="img" aria-label="Hand pointing at charts on a tablet" style="left:56px;top:564px;width:168px;height:149px;background:linear-gradient(135deg,#7fa8c8,#e8eef3 50%,#c9d6e0)"></div>
<div class="photo" role="img" aria-label="Business people holding a smartphone" style="left:238px;top:564px;width:168px;height:149px;background:linear-gradient(135deg,#c79a72,#3a3d48 50%,#9ab6cf)"></div>
<div class="blue-head" style="left:56px;top:728px;width:170px">MALESUADA NUNC VITAEMI EROS LOREM SUSPE</div>
<div class="blue-head" style="left:238px;top:728px;width:170px">MALESUADA NUNC VITAEMI EROS LOREM SUSPE</div>
<p class="copy" style="left:56px;top:764px;width:168px">Suspendisse elementum maximus turpis vel susci pit. Nullam dapibus, ligula vitae feugiat hendrerit, nisl neque gravida nunc, sed viverra dui augue eget libero. Nulla ut quam lacus. Proin lac Aliquam…</p>
<p class="copy" style="left:238px;top:764px;width:168px">Suspendisse elementum maximus turpis vel susci pit. Nullam dapibus, ligula vitae feugiat hendrerit, nisl neque gravida nunc, sed viverra dui augue eget libero. Nulla ut quam lacus. Proin lac Aliquam…</p>
<div class="news-rule" style="left:56px;top:824px;width:166px"></div>
<div class="news-rule" style="left:238px;top:824px;width:166px"></div>
<a class="read-more" style="left:175px;top:835px">READ MORE</a>
<a class="read-more" style="left:357px;top:835px">READ MORE</a>

<h2 class="section-title" style="left:430px;top:165px;width:167px">BLOGGER</h2>
<article class="blog-item" style="top:205px;height:81px">
  <div class="thumb" role="img" aria-label="Smartwatch on a wrist" style="background:linear-gradient(135deg,#c9d3dc,#3b4e6c)"></div>
  <h3>Lorem ipsum dolor sit amet cons</h3>
  <p>Lorem ipsum dolor sit amet conse ctetur adipisicing elit, sed do eiusmod tempor…</p>
</article>
<article class="blog-item" style="top:296px;height:81px">
  <div class="thumb" role="img" aria-label="Red and black headphones" style="background:radial-gradient(circle,#d02a2a,#222 70%,#eee)"></div>
  <h3>Ctetur adipiscing elit, sed do eiusmod</h3>
  <p>Lorem ipsum dolor sit amet conse ctetur adipisicing elit, sed do eiusmod tempor…</p>
</article>
<article class="blog-item" style="top:387px;height:81px">
  <div class="thumb" role="img" aria-label="Analog wristwatch" style="background:linear-gradient(135deg,#f2f2f2,#c9b49a)"></div>
  <h3>Tempor incididunt ut labore et</h3>
  <p>Lorem ipsum dolor sit amet conse ctetur adipisicing elit, sed do eiusmod tempor…</p>
</article>
<article class="blog-item" style="top:478px;height:81px">
  <div class="thumb" role="img" aria-label="Action camera" style="background:radial-gradient(circle,#3a4d62,#cfd4d8 75%)"></div>
  <h3>Reprehenderit in voluptate velit</h3>
  <p>Lorem ipsum dolor sit amet conse ctetur adipisicing elit, sed do eiusmod tempor…</p>
</article>
<article class="blog-item" style="top:570px;height:81px">
  <div class="thumb" role="img" aria-label="Two smartwatches" style="background:linear-gradient(90deg,#2c2c2c,#e8e8e8 50%,#5a3a5e)"></div>
  <h3>Esse cillum dolore eu fugiat nulla pariatu</h3>
  <p>Lorem ipsum dolor sit amet conse ctetur adipisicing elit, sed do eiusmod tempor…</p>
</article>
<article class="blog-item" style="top:661px;height:97px">
  <div class="thumb" role="img" aria-label="Row of smartphones" style="background:linear-gradient(90deg,#222,#6b6b6b 50%,#1a1a1a)"></div>
  <h3>Sint occaecat cupidatat non proiden</h3>
  <p>Lorem ipsum dolor sit amet conse ctetur adipisicing elit, sed do eiusmod tempor…</p>
</article>

<aside class="popular">
  <div class="popular-head">POPULAR ELECTRONICS OF THE MOUNTH</div>
  <div class="popular-list">
    <div class="product" role="img" aria-label="Silver camcorder" style="background:radial-gradient(ellipse at center,#c9cdd2,#fff 70%)"></div>
    <div class="product" role="img" aria-label="3D television" style="background:radial-gradient(ellipse at center,#4a8ed0,#1d2230 60%,#fff 72%)"></div>
    <div class="product" role="img" aria-label="Three smartphones" style="background:radial-gradient(ellipse at center,#6c9ed6,#222 55%,#fff 72%)"></div>
    <div class="product" role="img" aria-label="DSLR camera with flash" style="background:radial-gradient(ellipse at center,#3a3a3a,#9a9a9a 45%,#fff 70%)"></div>
    <div class="product" role="img" aria-label="Professional video camera" style="background:radial-gradient(ellipse at center,#2a2a2a,#777 45%,#fff 70%)"></div>
  </div>
</aside>

<footer class="site-footer">
  <h4 class="foot-head" style="left:56px">NAVIGATION</h4>
  <ul class="foot-list" style="left:56px">
    <li>Home</li><li class="current">About</li><li>News</li><li>Reviews</li><li>Contacts</li>
  </ul>
  <h4 class="foot-head" style="left:180px">CATEGORIES</h4>
  <ul class="foot-list" style="left:180px">
    <li>Appliances</li><li>Audio</li><li>Cameras</li><li>Car Tech</li><li>Desktops</li><li>Headphones</li><li>Laptops</li>
  </ul>
  <ul class="foot-list" style="left:304px">
    <li>Networking</li><li>Phones</li><li>Printers</li><li>Software</li><li>Tablets</li><li>TVs</li>
  </ul>
  <h4 class="foot-head" style="left:429px">FOLLOW US</h4>
  <div class="social" style="top:54px"><div class="dot"></div><span>FRIENDNEST</span></div>
  <div class="social" style="top:87px"><div class="dot"></div><span>CHIRPLINE</span></div>
  <div class="social" style="top:119px"><div class="dot"></div><span>RSS</span></div>
  <div class="foot-rule"></div>
  <div class="copyright">Handset Den © 2016 . Privacy Policy</div>
  <svg class="to-top" width="33" height="33" viewBox="0 0 33 33"><circle cx="16.5" cy="16.5" r="15" fill="none" stroke="#1d4fc9" stroke-width="2.5"/><circle cx="16.5" cy="16.5" r="10" fill="#1d4fc9"/><path d="M16.5 10.5 L11 16 H14.5 V22 H18.5 V16 H22 Z" fill="#1c1c1c"/></svg>
</footer>

</body>
</html>
```